Chamber of Commerce Web Design Project

We are working with Marigold Chamber of Commerce. They are a new chamber of commerce forming in SoCal.
Some sites to use for inspiration:
https://brevenlochamber.org
https://varnidel.org
https://www.quoratlinchamber.com
https://www.wtchamber.com
https://morvendipcc.org
Thank you for taking the time to consider designing a website for us. We are web developers based in Stockton, CA, USA. Most of our projects go through the same process. Understanding this process may help you win a project with us. We custom-code all of our websites in-house. We don’t have any requirements as to what tools you use for your design, but we prefer Figma files. For any design that we label as four-stars, we send it to the client for review. The client picks the final design they want us to use. Once we complete this process, we will continue to show additional clients all the four-star sites and purchase them later. Your designs will have multiple chances to sell. For better chances of success, we ask that you follow these guidelines.
IMAGES:
If you use any images or icons in the design, we ask that you have a link to the asset so we can purchase the image/icon. Most of the designs we submit do not have the customer’s images on them unless they have some great images. Be creative; show us the feeling you are trying to portray with your image choices. Use any royalty-free site you choose. We subscribe to Adobe and mainly use their images, but we can purchase images outside of Adobe.
PLEASE NOTE: we will not submit designs to clients with watermarks on the images.
FONTS:
We ask that you identify the fonts used in the design. This can be done in a message if you want. We typically use Google Fonts and Adobe Fonts.
CONTENT:
We're always open to different content and ideas. We often submit designs with stock images so the client can see our vision. We typically take pictures after the website launch to use their images with our vision. Lorem Ipsum is fine for paragraphs, but we ask that you write the headers in correct English. We want to be able to show the vision and identify the sections of the website.
INSPIRATION:
We typically add a couple of links in the brief of websites we like to help you get started in your design.
REVISIONS:
We do not often ask for revisions of the designs unless we see something in the design that may not appeal to the client. If there are slight changes that we want to make, we do that in the development process.
FEEDBACK:
We rarely give feedback on designs during the design process. We are working on many website projects and do not have the time to provide feedback. We usually respond if your request is well thought out and asks specific questions, but a note asking “feedback, please” usually goes unanswered.

```html
<!DOCTYPE html>
<html lang="en">
<head>
<meta charset="utf-8">
<title>Marigold Chamber of Commerce</title>
<link href="https://fonts.googleapis.com/css2?family=Oswald:wght@500;600;700&family=Poppins:wght@400;500;600&display=swap" rel="stylesheet">
<style>
:root{
  --blue:#1a82f0;
  --blue-dark:#0f6fd8;
  --ink:#222629;
  --text:#474b50;
  --muted:#8a8f95;
  --grey-bg:#f4f4f4;
  --gold:#f5c21b;
  --line:#d9dde2;
  --white:#ffffff;
}
*{margin:0;padding:0;box-sizing:border-box}
html,body{width:1200px;height:4773px;overflow:hidden}
body{position:relative;font-family:"Poppins",sans-serif;color:var(--text);background:var(--white)}
.abs{position:absolute}
.section{position:absolute;left:0;width:1200px}
.heading{font-family:"Oswald",sans-serif;font-weight:700;color:var(--ink);text-transform:uppercase;letter-spacing:-0.5px;line-height:1}
.eyebrow{font-size:19px;color:var(--blue);font-weight:500;text-transform:uppercase;display:flex;align-items:center;gap:10px}
.eyebrow .dash{display:inline-block;width:46px;height:2px;background:var(--blue)}
.center{left:0;width:1200px;text-align:center}
.para{font-size:13.5px;line-height:24px;color:var(--text)}
.btn{display:flex;align-items:center;justify-content:space-between;background:var(--blue);color:var(--white);border-radius:20px;font-size:15px;font-weight:500;padding:0 14px 0 14px;text-transform:uppercase}
.btn .go{width:16px;height:16px;border-radius:50%;background:var(--gold);display:flex;align-items:center;justify-content:center}
.btn .go svg{width:8px;height:8px}
.brand{display:flex;align-items:center;gap:10px;font-family:"Oswald",sans-serif;font-weight:600;text-transform:uppercase;line-height:1}
.brand .mark{border-radius:50%}
.brand .name{display:flex;flex-direction:column}
.photo{position:absolute}

/* header */
.site-header{top:0;height:152px;background:var(--white)}
.site-header .brand{left:67px;top:38px;color:var(--blue)}
.site-header .brand .mark{width:54px;height:54px;background:var(--gold)}
.site-header .brand .big{font-size:40px}
.site-header .brand .small{font-size:14px;letter-spacing:0.6px;margin-top:3px}
.nav a{position:absolute;top:72px;font-size:13px;color:var(--ink);text-decoration:none;text-transform:uppercase}
.nav a.active{color:var(--blue)}
.nav a.active::after{content:"";position:absolute;left:6px;right:6px;bottom:-8px;height:1px;background:var(--blue)}
.nav .cta{top:64px;height:32px;width:106px;left:1028px;border-radius:16px;background:var(--blue);color:var(--white);display:flex;align-items:center;justify-content:center}

/* hero */
.hero{top:152px;height:694px;overflow:hidden}
.hero .photo{inset:0;background:linear-gradient(100deg,#e9eff6 0%,#dfe8f1 35%,#b9c9da 60%,#8aa4c0 80%,#c8d6e4 100%)}
.hero .welcome{left:67px;top:128px;font-size:22px;color:var(--ink);text-transform:uppercase;font-weight:500}
.hero .title{left:64px;top:168px;font-size:98px;color:var(--blue)}
.hero .subtitle{left:67px;top:267px;font-size:36px;color:#5b6168;font-weight:600}
.hero .lead{left:67px;top:352px;width:430px;font-size:20px;line-height:31px;color:var(--ink)}
.hero .btn{left:74px;top:441px;width:172px;height:40px;font-size:17px;border-radius:20px}
.dots{left:548px;top:652px;display:flex;gap:14px;align-items:center}
.dots span{width:12px;height:12px;border-radius:50%;background:var(--white)}
.dots span.on{background:var(--blue);box-shadow:0 0 0 3px var(--white)}

/* accelerator */
.accelerator{top:846px;height:532px}
.accelerator .heading{top:76px;font-size:44px}
.rule{position:absolute;height:3px;background:var(--blue)}
.accelerator .intro{left:200px;top:156px;width:800px;text-align:center;font-size:14px;line-height:22px}
.pillar{position:absolute;top:243px;width:260px;text-align:center}
.pillar h3{margin-top:26px;font-weight:500;font-size:25px;color:var(--ink)}
.pillar .bar{width:34px;height:2px;background:var(--gold);margin:6px auto 14px}
.pillar p{font-size:13.5px;line-height:22px}
.icon-ring{width:82px;height:82px;border-radius:50%;background:var(--blue);margin:0 auto;display:flex;align-items:center;justify-content:center;box-shadow:0 0 0 4px var(--white),0 0 0 7px #d3e5fb}
.icon-ring svg{width:40px;height:40px}

/* about */
.about{top:1378px;height:633px;background:var(--grey-bg)}
.about .photo{left:140px;top:117px;width:438px;height:438px;border-radius:50%;background:linear-gradient(180deg,#e6b84a 0%,#c9a05a 35%,#3f75b6 55%,#1f5aa3 100%);border:8px solid #3d8ae6}
.about .heading{left:654px;top:140px;font-size:56px}
.about .eyebrow{left:654px;top:197px}
.about .para{left:661px;top:254px;width:396px;text-align:justify}
.about .btn{left:661px;top:456px;width:154px;height:36px}

/* services */
.services{top:2011px;height:704px}
.services .heading{top:92px;font-size:56px}
.services .eyebrow{left:0;width:1200px;justify-content:center;top:150px}
.services .intro{left:240px;top:212px;width:720px;text-align:center;font-size:14px;line-height:24px}
.services .diagram{left:0;top:0;width:1200px;height:704px}
.service-label{position:absolute;font-size:16px;line-height:19px;color:var(--ink);font-weight:500}
.svc-icon{position:absolute;width:72px;height:72px;border-radius:50%;background:var(--blue);display:flex;align-items:center;justify-content:center;box-shadow:0 0 0 4px var(--white),0 0 0 6px #cfe2fa}
.svc-icon svg{width:36px;height:36px}
.core-name{position:absolute;left:440px;top:520px;width:320px;text-align:center;color:var(--white);font-family:"Oswald",sans-serif;font-weight:600;text-transform:uppercase;line-height:1}
.core-name .big{font-size:44px}
.core-name .small{font-size:18px;margin-top:4px;letter-spacing:0.5px}

/* member resources */
.members{top:2715px;height:589px;background:var(--grey-bg)}
.members .block{left:824px;top:17px;width:376px;height:572px;background:var(--blue)}
.members .photo{left:578px;top:109px;width:555px;height:384px;background:linear-gradient(135deg,#cfd6dc 0%,#9aa6b0 45%,#5e6a74 75%,#b8c2ca 100%)}
.members .heading{left:69px;top:130px;font-size:56px}
.members .eyebrow{left:67px;top:192px}
.members .para{left:69px;top:258px;width:395px;text-align:justify}
.members .btn{left:72px;top:476px;width:128px;height:36px}

/* blog */
.blog{top:3304px;height:566px}
.blog .heading{top:124px;font-size:56px}
.blog .eyebrow{left:0;width:1200px;justify-content:center;top:182px}
.card{position:absolute;top:248px;width:311px;height:240px}
.card .photo{left:0;top:0;width:311px;height:196px}
.card .box{position:absolute;left:120px;top:96px;width:191px;padding:14px 8px 0 14px;background:var(--white);height:144px}
.card .date{font-size:11px;color:var(--muted)}
.card h4{font-size:20px;font-weight:400;color:var(--blue);margin:8px 0 4px}
.card .excerpt{font-size:12px;line-height:19px;color:var(--ink)}
.card .more{position:absolute;left:134px;top:262px;font-size:11px;font-style:italic;color:var(--blue)}
.arrow{position:absolute;top:3655px;width:42px;height:42px;border-radius:50%;background:#f1f2f4;display:flex;align-items:center;justify-content:center;border:1px solid #e3e5e8}
.arrow svg{width:12px;height:12px}

/* contact */
.contact{top:3870px;height:608px}
.contact .photo{left:69px;top:69px;width:453px;height:382px;background:linear-gradient(160deg,#c9b08a 0%,#a9967a 35%,#4d5a6a 65%,#9fb7c4 100%)}
.contact .heading{left:578px;top:63px;font-size:56px;display:flex;align-items:center;gap:14px}
.contact .heading .dash{width:46px;height:2px;background:var(--blue)}
.contact .intro{left:585px;top:145px;width:550px;font-size:13.5px;line-height:24px}
.field{position:absolute;border:1px solid var(--line);background:var(--white);font-size:13px;color:#6d7278;padding:0 20px;display:flex;align-items:center;box-shadow:0 1px 3px rgba(0,0,0,0.05)}
.field.area{align-items:flex-start;padding-top:20px}
.contact .btn{left:582px;top:475px;width:113px;height:37px}

/* footer */
.site-footer{top:4478px;height:295px;background:var(--blue);color:var(--white)}
.site-footer .brand{left:70px;top:58px;color:var(--white)}
.site-footer .brand .mark{width:40px;height:40px;background:var(--gold)}
.site-footer .brand .big{font-size:30px}
.site-footer .brand .small{font-size:11px;letter-spacing:0.4px;margin-top:2px}
.site-footer .about-text{left:70px;top:128px;width:220px;font-size:13px;line-height:20px}
.socials{left:72px;top:181px;display:flex;gap:5px}
.socials span{width:28px;height:28px;border:1px solid var(--white);border-radius:3px;display:flex;align-items:center;justify-content:center}
.socials span i{width:8px;height:8px;border-radius:50%;background:var(--white)}
.vdiv{position:absolute;top:62px;width:1px;height:26px;background:var(--white)}
.col-title{position:absolute;top:64px;font-size:15px;text-transform:uppercase}
.links a{position:absolute;left:384px;font-size:13px;color:var(--white);text-decoration:none;display:flex;align-items:center;gap:4px}
.links a::before{content:"";width:11px;height:11px;border-radius:50%;background:rgba(255,255,255,0.75)}
.c-item{position:absolute;left:624px;display:flex;gap:16px;font-size:12px;line-height:15px}
.c-item .ic{width:26px;height:26px;border:1px solid var(--white);border-radius:3px;display:flex;align-items:center;justify-content:center;flex-shrink:0}
.c-item .ic svg{width:13px;height:13px}
.news-text{left:941px;top:118px;width:200px;font-size:13px;line-height:18px}
.news-field{left:941px;top:172px;width:194px;height:28px;background:var(--white);border-radius:3px;color:#8a8f95;font-size:11px;display:flex;align-items:center;padding-left:8px}
.news-field .send{position:absolute;right:4px;top:4px;width:28px;height:20px;border-radius:8px;background:var(--blue);display:flex;align-items:center;justify-content:center}
.hdiv{left:70px;top:241px;width:1065px;height:1px;background:rgba(255,255,255,0.7)}
.copyright{left:0;width:1200px;text-align:center;top:262px;font-size:11px}
</style>
</head>
<body>

<header class="section site-header">
  <div class="abs brand">
    <span class="mark"></span>
    <span class="name"><span class="big">Marigold</span><span class="small">Chamber of Commerce</span></span>
  </div>
  <nav class="nav">
    <a class="active" style="left:404px">Home</a>
    <a style="left:502px">About Us</a>
    <a style="left:622px">Services</a>
    <a style="left:743px">Member Resources</a>
    <a style="left:933px">Events</a>
    <a class="cta">Contact Us</a>
  </nav>
</header>

<section class="section hero">
  <div class="photo" role="img" aria-label="Industrial pipelines and steel supports under a bright sky"></div>
  <div class="abs welcome">Welcome to</div>
  <h1 class="abs heading title">Marigold</h1>
  <div class="abs heading subtitle">Chamber of Commerce</div>
  <p class="abs lead">Lorem ipsum dolor sit amet, consectetur adipiscing elit, sed do eiusmod tempor</p>
  <a class="abs btn">Contact Us <span class="go"><svg viewBox="0 0 8 8"><path d="M2 1l4 3-4 3z" fill="#1a82f0"/></svg></span></a>
  <div class="abs dots"><span class="on"></span><span></span><span></span><span></span></div>
</section>

<section class="section accelerator">
  <h2 class="abs center heading">Your Business Accelerator</h2>
  <div class="rule" style="left:580px;top:125px;width:40px"></div>
  <p class="abs intro">Lorem ipsum dolor sit amet, consectetur adipiscing elit, sed do eiusmod tempor incididunt ut labore et dolore magna aliqua. Quis ipsum suspendisse ultrices gravida. Risus commodo viverra maecenas accumsan lacus vel facilisis.</p>
  <div class="pillar" style="left:140px">
    <div class="icon-ring"><svg viewBox="0 0 40 40" fill="none" stroke="#fff" stroke-width="2"><circle cx="20" cy="20" r="7"/><circle cx="20" cy="6" r="3"/><circle cx="8" cy="28" r="3"/><circle cx="32" cy="28" r="3"/><path d="M17 20l2 2 4-4"/></svg></div>
    <h3>Convene</h3><div class="bar"></div>
    <p>Lorem ipsum dolor sit amet,<br>consectetur adipiscing elit.</p>
  </div>
  <div class="pillar" style="left:470px">
    <div class="icon-ring"><svg viewBox="0 0 40 40" fill="none" stroke="#fff" stroke-width="2"><rect x="8" y="8" width="24" height="24" rx="3"/><path d="M14 26l12-12M18 14h8v8"/></svg></div>
    <h3>Navigate</h3><div class="bar"></div>
    <p>Lorem ipsum dolor sit amet,<br>consectetur adipiscing elit.</p>
  </div>
  <div class="pillar" style="left:805px">
    <div class="icon-ring"><svg viewBox="0 0 40 40" fill="none" stroke="#fff" stroke-width="2"><path d="M8 16h10l8-6v20l-8-6H8z"/><path d="M30 15c2 2 2 8 0 10M12 24l2 8"/></svg></div>
    <h3>Advocate</h3><div class="bar"></div>
    <p>Lorem ipsum dolor sit amet,<br>consectetur adipiscing elit.</p>
  </div>
</section>

<section class="section about">
  <div class="photo" role="img" aria-label="Group of business professionals inside a circular frame above stylised waves"></div>
  <h2 class="abs heading">About Us</h2>
  <div class="abs eyebrow">Who We Are <span class="dash"></span></div>
  <p class="abs para">Lorem ipsum dolor sit amet, consectetur adipiscing elit, sed do eiusmod tempor incididunt ut labore et dolore magna aliqua. Quis ipsum suspendisse ultrices gravida. Risus commodo viverra maecenas accumsan lacus vel facilisis. Lorem ipsum dolor sit amet, consectetur adipiscing elit, sed do eiusmod tempor incididunt ut labore et dolore magna aliqua.</p>
  <a class="abs btn">Know More <span class="go"><svg viewBox="0 0 8 8"><path d="M2 1l4 3-4 3z" fill="#1a82f0"/></svg></span></a>
</section>

<section class="section services">
  <h2 class="abs center heading">Our Services</h2>
  <div class="abs eyebrow"><span class="dash"></span> What We Do <span class="dash"></span></div>
  <p class="abs intro">Lorem ipsum dolor sit amet, consectetur adipiscing elit, sed do eiusmod tempor incididunt ut labore et dolore magna aliqua. Quis ipsum suspendisse ultrices gravida. Risus commodo viverra maecenas</p>
  <svg class="abs diagram" viewBox="0 0 1200 704">
    <defs>
      <linearGradient id="coreFill" x1="0" y1="0" x2="1" y2="1">
        <stop offset="0" stop-color="#2c3440"/><stop offset="0.6" stop-color="#5a4a3c"/><stop offset="1" stop-color="#8a7a66"/>
      </linearGradient>
    </defs>
    <path d="M370 632 A230 230 0 0 1 830 632" fill="none" stroke="#e7e9ec" stroke-width="2"/>
    <path d="M394 632 A206 206 0 0 1 806 632 Z" fill="url(#coreFill)" role="img" aria-label="Business people in a meeting room"/>
    <g fill="#f5c21b">
      <circle cx="534" cy="414" r="3"/><circle cx="674" cy="418" r="3"/>
      <circle cx="436" cy="488" r="3"/><circle cx="760" cy="490" r="3"/>
      <circle cx="377" cy="612" r="3"/><circle cx="822" cy="612" r="3"/>
    </g>
  </svg>
  <div class="core-name"><div class="big">Marigold</div><div class="small">Chamber of Commerce</div></div>

  <div class="svc-icon" style="left:490px;top:331px"><svg viewBox="0 0 36 36" fill="none" stroke="#fff" stroke-width="2"><rect x="6" y="9" width="20" height="16" rx="2"/><path d="M10 21v-4M15 21v-7M20 21v-5M22 6h8v6h-8z"/></svg></div>
  <div class="service-label" style="left:374px;top:334px;text-align:right">Marketing<br>Consultation</div>

  <div class="svc-icon" style="left:662px;top:338px"><svg viewBox="0 0 36 36" fill="none" stroke="#fff" stroke-width="2"><circle cx="18" cy="18" r="11"/><circle cx="18" cy="15" r="3"/><path d="M12 25c1-4 11-4 12 0"/></svg></div>
  <div class="service-label" style="left:742px;top:334px">Government<br>Relations</div>

  <div class="svc-icon" style="left:349px;top:420px"><svg viewBox="0 0 36 36" fill="none" stroke="#fff" stroke-width="2"><circle cx="15" cy="15" r="8"/><path d="M21 21l8 8M11 16l3-3 3 3 3-4"/></svg></div>
  <div class="service-label" style="left:258px;top:440px;text-align:right">Market<br>Research</div>

  <div class="svc-icon" style="left:775px;top:425px"><svg viewBox="0 0 36 36" fill="none" stroke="#fff" stroke-width="2"><rect x="9" y="11" width="18" height="14" rx="2"/><path d="M14 11V8h8v3M9 17h18"/></svg></div>
  <div class="service-label" style="left:848px;top:430px">Small Business<br>Support</div>

  <div class="svc-icon" style="left:290px;top:559px"><svg viewBox="0 0 36 36" fill="none" stroke="#fff" stroke-width="2"><circle cx="18" cy="18" r="4"/><circle cx="8" cy="10" r="2.5"/><circle cx="28" cy="10" r="2.5"/><circle cx="8" cy="26" r="2.5"/><circle cx="28" cy="26" r="2.5"/><path d="M10 12l5 4M26 12l-5 4M10 24l5-4M26 24l-5-4"/></svg></div>
  <div class="service-label" style="left:182px;top:580px;text-align:right">Business<br>Connections</div>

  <div class="svc-icon" style="left:831px;top:555px"><svg viewBox="0 0 36 36" fill="none" stroke="#fff" stroke-width="2"><circle cx="18" cy="18" r="11"/><circle cx="18" cy="18" r="5"/><path d="M18 7v4M18 25v4M7 18h4M25 18h4"/></svg></div>
  <div class="service-label" style="left:915px;top:580px">Talent &amp;<br>Workforce</div>
</section>

<section class="section members">
  <div class="abs block"></div>
  <div class="photo" role="img" aria-label="Business team walking together through a bright modern walkway"></div>
  <h2 class="abs heading">Member Resources</h2>
  <div class="abs eyebrow" style="text-transform:uppercase">Marigold Chamber of Commerce <span class="dash"></span></div>
  <p class="abs para">Lorem ipsum dolor sit amet, consectetur adipiscing elit, sed do eiusmod tempor incididunt ut labore et dolore magna aliqua. Quis ipsum suspendisse ultrices gravida. Risus commodo viverra maecenas accumsan lacus vel facilisis. Lorem ipsum dolor sit amet, consectetur adipiscing elit, sed do eiusmod tempor incididunt ut labore et dolore magna aliqua.</p>
  <a class="abs btn">Explore <span class="go"><svg viewBox="0 0 8 8"><path d="M2 1l4 3-4 3z" fill="#1a82f0"/></svg></span></a>
</section>

<section class="section blog">
  <h2 class="abs center heading">Latest Blog</h2>
  <div class="abs eyebrow"><span class="dash"></span> News &amp; Updates <span class="dash"></span></div>

  <article class="card" style="left:83px">
    <div class="photo" role="img" aria-label="Small business owner in a shop" style="background:linear-gradient(135deg,#8a8f95,#c9a08c 55%,#d8dde2)"></div>
    <div class="box"><div class="date">Friday JAN 24, 2025</div><h4>Post 1 Headline</h4><p class="excerpt">Lorem ipsum dolor sit amet, consectetur adipi</p></div>
    <a class="more">Read More</a>
  </article>
  <article class="card" style="left:444px">
    <div class="photo" role="img" aria-label="Two colleagues discussing work at a desk" style="background:linear-gradient(135deg,#4e8a80,#b8b0a6 55%,#e3e6e8)"></div>
    <div class="box"><div class="date">Saturday JAN 25, 2025</div><h4>Post 2 Headline</h4><p class="excerpt">Lorem ipsum dolor sit amet, consectetur adipi</p></div>
    <a class="more">Read More</a>
  </article>
  <article class="card" style="left:804px">
    <div class="photo" role="img" aria-label="Business meeting around a conference table" style="background:linear-gradient(135deg,#c7a58e,#6a7580 50%,#dfe3e7)"></div>
    <div class="box"><div class="date">Friday JAN 25, 2023</div><h4>Post 3 Headline</h4><p class="excerpt">Lorem ipsum dolor sit amet, consectetur adipi</p></div>
    <a class="more">Read More</a>
  </article>
</section>
<div class="arrow" style="left:22px"><svg viewBox="0 0 12 12"><path d="M8 2L4 6l4 4" fill="none" stroke="#333" stroke-width="1.5"/></svg></div>
<div class="arrow" style="left:1146px"><svg viewBox="0 0 12 12"><path d="M4 2l4 4-4 4" fill="none" stroke="#333" stroke-width="1.5"/></svg></div>

<section class="section contact">
  <div class="photo" role="img" aria-label="Team of business professionals standing together in an office lobby"></div>
  <h2 class="abs heading">Contact Us <span class="dash"></span></h2>
  <p class="abs intro">Lorem ipsum dolor sit amet, consectetur adipiscing elit, sed do eiusmod tempor incid idunt ut labore et dolore magna aliqua. Quis ipsum suspendisse ultrices</p>
  <div class="field" style="left:582px;top:212px;width:268px;height:50px">Your Name</div>
  <div class="field" style="left:869px;top:212px;width:266px;height:50px">Phone Number</div>
  <div class="field" style="left:582px;top:275px;width:553px;height:52px">Email Address</div>
  <div class="field area" style="left:582px;top:340px;width:553px;height:98px">Message</div>
  <a class="abs btn">Submit <span class="go"><svg viewBox="0 0 8 8"><path d="M2 1l4 3-4 3z" fill="#1a82f0"/></svg></span></a>
</section>

<footer class="section site-footer">
  <div class="abs brand">
    <span class="mark"></span>
    <span class="name"><span class="big">Marigold</span><span class="small">Chamber of Commerce</span></span>
  </div>
  <p class="abs about-text">Lorem ipsum dolor sit amet, consectetur adipiscing elit</p>
  <div class="abs socials"><span><i></i></span><span><i></i></span><span><i></i></span><span><i></i></span></div>

  <div class="vdiv" style="left:372px"></div>
  <div class="col-title" style="left:384px">Quick Links</div>
  <nav class="links">
    <a style="top:115px">About Us</a>
    <a style="top:142px">Services</a>
    <a style="top:170px">Membership</a>
    <a style="top:198px">Contact Us</a>
  </nav>

  <div class="vdiv" style="left:613px"></div>
  <div class="col-title" style="left:624px">Contact Us</div>
  <div class="c-item" style="top:111px"><span class="ic"><svg viewBox="0 0 13 13"><path d="M3 1l2 3-1 1c1 2 2 3 4 4l1-1 3 2-1 2C6 12 1 7 1 2z" fill="#fff"/></svg></span><span>CALL US<br>XXXX XXX XXX</span></div>
  <div class="c-item" style="top:154px"><span class="ic"><svg viewBox="0 0 13 13"><rect x="1" y="3" width="11" height="7" fill="#fff"/><path d="M1 3l5.5 4L12 3" fill="none" stroke="#1a82f0"/></svg></span><span>EMAIL US<br>info@websitename.com</span></div>
  <div class="c-item" style="top:198px"><span class="ic"><svg viewBox="0 0 13 13"><path d="M6.5 1a4 4 0 0 1 4 4c0 3-4 7-4 7s-4-4-4-7a4 4 0 0 1 4-4z" fill="#fff"/><circle cx="6.5" cy="5" r="1.5" fill="#1a82f0"/></svg></span><span>Address line Dummy Here<br>Address line Here</span></div>

  <div class="vdiv" style="left:926px"></div>
  <div class="col-title" style="left:939px">Newsletter Sign Up</div>
  <p class="abs news-text">Subscribe our newsletter to get the latest news.</p>
  <div class="abs news-field">Enter Email Address<span class="send"><svg width="14" height="10" viewBox="0 0 14 10"><path d="M1 5h11M8 1l4 4-4 4" fill="none" stroke="#fff" stroke-width="1.5"/></svg></span></div>

  <div class="abs hdiv"></div>
  <p class="abs copyright">Copyright © 2025 All Rights Reserved By Company name</p>
</footer>

</body>
</html>
```